Beautiful & Elegant Digital Brochure Needed For Luxury Real Estate Development

Hello,

Our company is seeking a beautiful design for our real estate development that is currently being launched.

About The Project:
Development Name - Willow Crest Estate
Location - Charleston, S.C.
Low-Country Southern Style Architecture
Google "low-country" Charleston, SC to get an idea of the unique culture of the city
Google "willow crest tree" Charleston, SC to understand the branding

Other Digital Brochures that we love

http://www.fernvalehotels.example/cedarhollow/wp-content/uploads/sites/6/2014/08/adventures-brochure.pdf

Why we like it... We love the classy feeling the brochure portrays by using unique fonts and backgrounds (burlap textures). We also love the images that represent a "low-country" vibe.

Requirements:
1. We will be providing all of the content (attached)

2. Please use plenty of southern low-country stock images from PixelVaultStock (we have a subscription so just use the watermarked images unless you have full permissions)

3. Do not copy the Cedar Hollow brochure - create a unique vision that fits in to the low-country and southern vibe

4. Attached is our logos

The font we like to use is - Caslon Antique / italic
Thank you!

Project Deadline Extended Reason: We've added more design information and we need to get more designers to participate. Added Monday, May 30, 2016

Target Market(s)

High net worth individuals - each homesite will be over 6 million dollars USD

Industry/Entity Type

Real Estate Development

Font styles to use
Script
Other font styles liked:
• Caslon Antique & Italic

Colors
abd036
00a990
acd036
9bcb3c
33b8a4
86cfc6
cfeae6

Requirements
Must have
• low country feeling
Nice to have
• burlap, wood backgrounds
Should not have
• Should NOT be corporate. This brochure is for multi-millionaire home buyers and investors. They are seeking simple, beautiful, quiet, serene, and southern lifestyles on the Intracoastal waterway on Marley Isle, Charleston, South Carolina.

```html
<!DOCTYPE html>
<html lang="en">
<head>
<meta charset="utf-8">
<title>Willow Crest Estate – Brochure</title>
<link href="https://fonts.googleapis.com/css2?family=Great+Vibes&family=IM+Fell+DW+Pica:ital@0;1&family=Lato:ital,wght@0,400;0,700;1,400;1,700&display=swap" rel="stylesheet">
<style>
  :root{
    --stage:#e8e3db;
    --paper:#ffffff;
    --ink:#2b2b2b;
    --mint:#cfeae6;
    --mint-soft:#e4f4f1;
    --green:#9bcb3c;
    --green-light:#abd036;
    --gold:#d9a520;
    --gold-light:#f3cf4a;
    --gold-deep:#b97c12;
    --black:#0c0c0c;
    --logo-text:#f2f2f2;
    --burlap:#e9e2d6;
    --burlap-dark:#d8cfc0;
  }
  *{box-sizing:border-box;margin:0;padding:0}
  html,body{width:1200px;height:900px;overflow:hidden}
  body{background:var(--stage);position:relative;font-family:"Lato",sans-serif;color:var(--ink)}

  .page{position:absolute;background:var(--paper);box-shadow:0 6px 18px rgba(0,0,0,.25);overflow:hidden}

  /* Cover */
  .cover{left:70px;top:125px;width:485px;height:685px}
  .cover-photo{position:absolute;left:0;top:0;width:100%;height:270px;
    background:linear-gradient(180deg,#6d6d68 0%,#c9c8c2 35%,#efefea 55%,#8f8e88 100%)}
  .silver-rule{position:absolute;left:0;width:100%;height:8px;
    background:linear-gradient(180deg,#f4f4f4,#a9a9a9)}
  .logo-band{position:absolute;left:0;top:278px;width:100%;height:117px;
    background:linear-gradient(180deg,#2a2a2a 0%,var(--black) 60%,#1a1a1a 100%);
    display:flex;align-items:center;justify-content:center;gap:12px}
  .logo-mark{width:14px;height:14px;border-radius:50%;background:var(--logo-text)}
  .logo-name{font-family:"Lato",sans-serif;font-weight:400;font-size:28px;color:var(--logo-text)}
  .burlap{position:absolute;left:0;top:403px;width:100%;height:282px;
    background:radial-gradient(ellipse at 50% 40%,#f3efe8 0%,var(--burlap) 55%,var(--burlap-dark) 100%)}
  .cover-title{position:absolute;left:0;top:76px;width:100%;text-align:center;
    font-family:"Great Vibes",cursive;font-weight:400;font-size:40px;color:var(--ink)}
  .title-rule{position:absolute;left:75px;top:236px;width:335px;height:1px;background:#3a3a3a}
  .gold-band{position:absolute;left:0;top:182px;width:100%;height:62px;
    background:linear-gradient(90deg,var(--gold-deep) 0%,var(--gold) 25%,var(--gold-light) 70%,#f7dc63 100%);
    text-align:center;padding-top:5px}
  .gold-band p{font-family:Arial,"Helvetica",sans-serif;font-weight:700;font-size:19px;line-height:25px;color:#fff;
    text-shadow:1px 1px 2px rgba(0,0,0,.55)}

  /* Inside page */
  .inside{left:650px;top:110px;width:490px;height:695px}
  .inside-photo{position:absolute;left:0;top:0;width:100%;height:235px;
    background:linear-gradient(180deg,#9fc3e6 0%,#c7dbe9 30%,#7a8ea3 45%,#a94848 60%,#54707c 72%,#b5a48c 85%,#7f9a5a 100%)}
  .section{position:absolute;left:0;width:100%;padding:0 14px}
  .section p{font-size:7.4px;line-height:9.6px;font-style:italic;text-align:justify;margin-bottom:3px}
  .section.upright p{font-style:normal}
  .section p::first-letter{font-style:normal;font-weight:700;font-size:11px}
  .mint{background:var(--mint)}
  .mint-soft{background:var(--mint-soft)}
  .heading-bar{position:absolute;left:0;width:100%;height:16px;
    background:linear-gradient(90deg,var(--green) 0%,var(--green-light) 40%,rgba(171,208,54,.15) 100%);
    padding-left:16px;font-family:"IM Fell DW Pica",serif;font-style:italic;font-weight:400;font-size:12px;line-height:16px;color:#1f2a10}
  .two-col{display:flex;gap:14px}
  .two-col p{flex:1}
</style>
</head>
<body>

<article class="page cover">
  <div class="cover-photo" role="img" aria-label="Black and white photograph of a columned plantation house with a white portico and rocking chairs"></div>
  <div class="silver-rule" style="top:270px"></div>
  <div class="logo-band">
    <span class="logo-mark"></span>
    <span class="logo-name">Willow Crest Estate</span>
  </div>
  <div class="silver-rule" style="top:395px"></div>
  <div class="burlap" role="img" aria-label="Burlap texture background"></div>
  <h1 class="cover-title" style="top:479px">Willow Crest Estate</h1>
  <div class="title-rule" style="top:639px"></div>
  <div class="gold-band" style="top:585px">
    <p>Charleston, S.C.</p>
    <p>Low-Country Southern Style Architecture</p>
  </div>
</article>

<article class="page inside">
  <div class="inside-photo" role="img" aria-label="Photograph of colourful gingerbread cottages with porches and flowering hydrangeas"></div>

  <section class="section mint" style="top:245px;height:88px;padding-top:8px">
    <p>Nestled on pristine Marley Isle, the Willow Crest Estate Community is a truly enviable locale. An unspoiled maritime forest and the island's meandering coastline create a stunning natural backdrop while proximity to Charleston's world-class dining and superior shops means that you never have to sacrifice comfort or style. Within the community, eighteen large, private home sites offer ample space to gather in an intimate setting with family and friends while the forty acre common area provides space for large gatherings and community events. Private pools, equestrian activities, racquet sports, and golfing are among the many community-based amenities that will connect you to your neighbors. Whether you seek a peaceful escape for deep relaxation, to adopt the spirit of Southern hospitality, or to immerse yourself in the Lowcountry experience, Willow Crest is the perfect haven.</p>
  </section>

  <h2 class="heading-bar" style="top:345px">The Legend of the Willow Crest</h2>

  <section class="section upright" style="top:366px;height:80px">
    <p>The community is named for South Carolina's enchanting Willow Crest Tree, a centuries-old live oak located at the heart of Marley Isle. Although the exact age of the Willow Crest is unknown, estimates based on the tree's size and condition suggest that the coastal oak is between 700 and 1500 years old. The tree predates recorded history on the island and likely stood its ground long before the arrival of Captain Elias Marrow to the Americas. The ancient tree's massive, sprawling branches reach outward in all directions, covering more than 17,000 square feet of ground with its majestic shade. Standing more than 65 feet tall, the massive oak towers over the park that bears its name. This imposing beauty has become one of the area's most iconic natural wonders, drawing thousands of visitors each year. Situated amid a treasure trove of historic structures and man-made beauty, the park offers visitors a reminder of Mother Nature's strength, vitality, and splendor.</p>
  </section>

  <h2 class="heading-bar" style="top:452px">Embrace Outdoor Living and Connect with Nature</h2>

  <section class="section mint-soft two-col" style="top:470px;height:100px;padding-top:6px">
    <p>Life is better when lived outdoors and in the Lowcountry, nature beckons. Wake each morning to breathtaking sunrises and allow the warm, salt-kissed air to rejuvenate your soul. Spend your days enjoying one of the area's exquisite beaches or visit some of Charleston's inspiring heritage sites. During the early evenings, enjoy dinner alfresco before retiring on the veranda with family and friends. Gather around an outdoor fireplace to share the day's memories and create even more under the stars.</p>
    <p>Featuring both community and private docks, Willow Crest is a maritime paradise. Board your vessel to explore the tidal Harlow River separating Marley Isle from the mainland or follow the Intracoastal Waterway to the sea. For the adventurous, a kayak or canoe is an ideal means for exploring the intricacies of the island's elaborate coastal marshes. Sport fishers will be pleased to find the channels teeming with flounder, cobia, mackerel, tarpon, white shrimp, and blue crabs. Non-anglers will also appreciate the plentiful array of aquatic life and availability of fresh daily seafood.</p>
  </section>

  <section class="section mint" style="top:574px;height:110px;padding-top:6px">
    <p>Inland, Charleston County is home to stunning city gardens, immaculate local parks, and quaint nature trails. Terrestrial wildlife is plentiful on the island and even a short hike is likely to yield amazing photo opportunities. The island is heavily populated by South Carolina's state animal, the white tailed deer, which can be seen bounding through the wooded terrain year-round. Wild turkeys, gray fox, flying squirrels, raccoon, bobcats, and bear also call the island home. For bird watchers, a close eye on the skies will yield handsome rewards. Heron, osprey, bald eagles, red-tailed hawks, egrets, and wood storks all call the island home. Dozens of migratory species provide increased variety to an already impressive host of island regulars and are always a welcome herald to the changing seasons.</p>
    <p>Despite seeing an influx of visitors and new residents, a strong commitment to ecologically conscious growth promises that this natural wonderland will remain intact for generations to come. Coastal management, wildlife conservation, and the protection of the area's natural resources are paramount among the considerations and development is conducted responsibly and respectfully.</p>
  </section>
</article>

</body>
</html>
```